2020 Fernhollow Summer Camp Brochure

We are wanting to design a brochure to be used for our Christian Summer Camp. This brochure will be used to attract new campers and current campers. We would like for it to be fun and exciting. It will be 11 x 8.5 folded. It could be either in portrait or landscape format. We have uploaded a document that has all the information that will need to be included. Also, we have uploaded several pictures that can be used. We would love for the back cover to have a design for our theme (see information sheet for more details).

Target Market(s)

Ages 8 - 18 and parents

Colors

Designer to choose colors to be used in the design.

Requirements
Must have
• The information included in document.
Nice to have
• Design for our theme on back

```html
<!DOCTYPE html>
<html lang="en">
<head>
<meta charset="utf-8">
<title>Camp Fernhollow – Summer Camp Brochure</title>
<link rel="stylesheet" href="https://fonts.googleapis.com/css2?family=Amatic+SC:wght@400;700&family=Archivo+Black&family=Figtree:wght@400;700&display=swap">
<style>
:root{
  --bg:#0c833f;
  --red:#7a1518;
  --white:#ffffff;
  --grey:#e7e7e8;
  --yellow:#f6e32b;
  --ink:#444;
}
*{margin:0;padding:0;box-sizing:border-box}
html,body{width:1200px;height:2238px;overflow:hidden;background:var(--bg)}
body{position:relative;font-family:"Figtree",sans-serif}
.panel{position:absolute;left:301px;width:598px;height:461px;overflow:hidden;background:var(--white)}
.cover{top:172px}
.collage{top:668px}
.info{top:1163px}
.mailer{top:1659px}

/* cover */
.photo{position:absolute;inset:0}
.cover .photo{background:linear-gradient(160deg,#9bb870 0%,#5e7f3a 40%,#7a5a3a 65%,#a9c46f 100%)}
.top-strip{position:absolute;left:0;top:0;width:100%;height:8px;background:var(--red)}
.name-tag{position:absolute;left:20px;top:22px;width:206px;height:62px;background:var(--white);border-radius:30px 8px 30px 10px}
.brand{font-family:"Archivo Black",sans-serif;color:var(--red);line-height:.95;text-transform:uppercase;white-space:nowrap}
.name-tag .brand{position:absolute;left:24px;top:12px;font-size:19px}
.disc{position:absolute;border-radius:50%;display:flex;align-items:center;justify-content:center;text-align:center;font-family:"Amatic SC",sans-serif;color:var(--white);text-transform:uppercase}
.cover .disc{left:182px;top:201px;width:244px;height:244px;background:rgba(122,21,24,.92);font-size:96px;line-height:.85;font-weight:700}

/* collage */
.collage .photo{background:linear-gradient(135deg,#5d6a3a 0%,#3e5b67 30%,#b8603a 55%,#d9d4cf 80%,#6f8a4a 100%)}
.ring{position:absolute;left:185px;top:116px;width:226px;height:226px;border-radius:50%;background:var(--red)}
.ring-inner{position:absolute;left:197px;top:128px;width:202px;height:202px;border-radius:50%;background:var(--white)}
.collage .disc{left:205px;top:136px;width:186px;height:186px;background:var(--red);font-size:30px;line-height:1.05}

/* info */
.headline{position:absolute;left:0;top:32px;width:100%;text-align:center;font-family:"Amatic SC",sans-serif;font-weight:400;color:var(--red);font-size:38px;line-height:1.05;text-transform:uppercase}
.activities{position:absolute;left:100px;width:398px;top:161px;text-align:center;color:var(--red);font-size:13.5px;line-height:1.3}
.ages{position:absolute;left:92px;top:240px;width:146px;height:146px}
.ages svg{position:absolute;inset:0}
.ages-text{position:absolute;left:0;top:22px;width:100%;text-align:center;font-family:"Amatic SC",sans-serif;color:var(--red);text-transform:uppercase}
.ages-text .big{font-size:38px;line-height:1}
.ages-text .small{font-size:21px;line-height:.98}
.sessions{position:absolute;left:247px;top:240px;width:261px;color:var(--red);font-size:10.3px}
.sessions-head{display:flex;align-items:center;font-weight:700;font-size:10.5px;height:12px}
.sessions-head::after{content:"";flex:1;height:3px;background:var(--red);margin-left:4px}
.sessions table{width:100%;border-collapse:collapse}
.sessions td{height:13.2px;border-bottom:1px solid #c9b0b0;white-space:nowrap}
.sessions td.price{font-weight:700;text-align:left;width:30px}
.sessions td.date{width:102px}
.register-band{position:absolute;left:0;top:405px;width:100%;height:43px;background:var(--grey)}
.register{position:absolute;left:105px;top:405px;width:387px;height:43px;display:flex;align-items:center;justify-content:center;font-family:"Amatic SC",sans-serif;font-size:26px;color:var(--white);text-transform:uppercase;letter-spacing:.5px;white-space:nowrap}
.register svg{position:absolute;inset:0}
.register span{position:relative}
.register .url{color:var(--yellow);margin-left:8px}

/* mailer */
.return{position:absolute;left:26px;top:30px;color:var(--ink);font-size:11.5px;line-height:1.18}
.return .brand{font-size:17px;margin-bottom:2px}
.return p{margin-left:2px}
.indicia{position:absolute;left:479px;top:27px;width:92px;height:92px;border:1.5px solid var(--ink);display:flex;align-items:center;justify-content:center;text-align:center;font-size:11px;line-height:1.2;color:var(--ink)}
.water{position:absolute;left:0;top:0;width:100%;height:100%}
.theme-art{position:absolute;left:236px;top:94px;width:128px;height:312px;background:linear-gradient(180deg,#9a3a3c 0%,#d9b9ba 100%)}
</style>
</head>
<body>

<section class="panel cover">
  <div class="photo" role="img" aria-label="Photo of two young campers riding horses in a sunny green paddock"></div>
  <div class="top-strip"></div>
  <div class="name-tag"><div class="brand">Camp<br>Fernhollow</div></div>
  <div class="disc">Summer<br>Camp</div>
</section>

<section class="panel collage">
  <div class="photo" role="img" aria-label="Collage of camp photos: jumping into the lake, campers in life vests on the blob, archery by an autumn overlook, and a shaving cream game"></div>
  <div class="ring"></div>
  <div class="ring-inner"></div>
  <div class="disc">Experience<br>summer like<br>never before, at<br>Camp Fernhollow!</div>
</section>

<section class="panel info">
  <h1 class="headline">Join us for a summer you will never<br>forget! Experience God in a new way.<br>Create life-long friendships.</h1>
  <p class="activities">Participate in our awesome activities: Archery Tag, Blob, Rappelling, Water Trampoline, Horses, Archery, Air Rifles, Fishing, Hiking, Arts and Crafts, and much more!</p>

  <div class="ages">
    <svg viewBox="0 0 146 146" aria-hidden="true">
      <path d="M22 4 Q8 4 8 18 L8 60 Q8 70 0 73 Q8 76 8 86 L8 128 Q8 142 22 142" fill="none" stroke="#7a1518" stroke-width="6"/>
      <path d="M124 4 Q138 4 138 18 L138 60 Q138 70 146 73 Q138 76 138 86 L138 128 Q138 142 124 142" fill="none" stroke="#7a1518" stroke-width="6"/>
    </svg>
    <div class="ages-text">
      <div class="big">Ages 8–18</div>
      <div class="small">11-Day Sessions<br>7-Day Sessions<br>4-Day Session</div>
    </div>
  </div>

  <div class="sessions">
    <div class="sessions-head">SESSIONS:</div>
    <table>
      <tr><td>Session 1 (11-Day)</td><td class="date">5/31/20 - 6/6/20</td><td class="price">$285</td></tr>
      <tr><td>Short Session 1 (4-Day)</td><td class="date">5/31/20 - 6/3/20</td><td class="price">$180</td></tr>
      <tr><td>Session 2 (11-Day)</td><td class="date">6/07/20 - 6/18/20</td><td class="price">$425</td></tr>
      <tr><td>Session 2B (7-Day)</td><td class="date">6/07/20 - 6/13/20</td><td class="price">$285</td></tr>
      <tr><td>Session 3 (11-Day)</td><td class="date">6/28/20 - 7/9/20</td><td class="price">$425</td></tr>
      <tr><td>Session 3B (7-Day)</td><td class="date">6/28/20 - 7/4/20</td><td class="price">$285</td></tr>
      <tr><td>Session 4 (11-Day)</td><td class="date">7/12/20 - 7/23/20</td><td class="price">$425</td></tr>
      <tr><td>Session 4B (7-Day)</td><td class="date">7/12/20 - 7/18/20</td><td class="price">$285</td></tr>
      <tr><td>Session 5 (7-Day)</td><td class="date">7/26/20 - 8/1/20</td><td class="price">$285</td></tr>
      <tr><td>Short Session 2 (4-Day)</td><td class="date">7/26/20 - 7/29/20</td><td class="price">$180</td></tr>
    </table>
  </div>

  <div class="register-band"></div>
  <div class="register">
    <svg viewBox="0 0 387 43" preserveAspectRatio="none" aria-hidden="true">
      <polygon points="0,0 387,0 372,21.5 387,43 0,43 15,21.5" fill="#7a1518"/>
    </svg>
    <span>Register today at</span><span class="url">campfernhollow.org</span>
  </div>
</section>

<section class="panel mailer">
  <svg class="water" viewBox="0 0 598 461" preserveAspectRatio="none" aria-hidden="true">
    <path d="M0 186 q7 -8 14 0 t14 0 t14 0 t14 0 t14 0 t14 0 t14 0 t14 0 t14 0 t14 0 t14 0 t14 0 t14 0 t14 0 t14 0 t14 0 t14 0 t14 0 t14 0 t14 0 t14 0 t14 0 t14 0 t14 0 t14 0 t14 0 t14 0 t14 0 t14 0 t14 0 t14 0 t14 0 t14 0 t14 0 t14 0 t14 0 t14 0 t14 0 t14 0 t14 0 t14 0 t14 0 t14 0 L598 461 L0 461 Z" fill="#7a1518"/>
  </svg>
  <div class="return">
    <div class="brand">Camp<br>Fernhollow</div>
    <p>PO Box 4410<br>Maple Ridge, AR<br>P: 501-555-0142<br>E: office@campfernhollow.org</p>
  </div>
  <div class="indicia">Non-Profit Org<br>U.S. Postage<br>PAID<br>Maple Ridge, AR<br>Permit #70</div>
  <div class="theme-art" role="img" aria-label="Theme illustration: an iceberg above and below the waterline, with a cross at its base"></div>
</section>

</body>
</html>
```